Business card design needed & Logo Design for Marketing

We need a business card design for a new beauty business. We offer Eyelash Extensions and beauty services, from our relaxing home based salon.

I would like the design to be modern and contemporary but with a twist of vintage thrown in. Our fave colour is Spearmint.

I also need a logo that can be embroidered onto uniforms.

Contact Information for Business Card

Velvet Bloom Beauty
Eyelash Extensions and Beauty Services
18 Windarra Court, Parkhurst 4815
0482615097

```html
<!DOCTYPE html>
<html lang="en">
<head>
<meta charset="utf-8">
<title>Velvet Bloom Beauty – Business Card</title>
<link href="https://fonts.googleapis.com/css2?family=Arimo:wght@400;700&display=swap" rel="stylesheet">
<style>
  :root {
    --paper: #f2f2f2;
    --ink: #231f20;
    --spearmint: #6cc8a8;
  }
  html, body {
    margin: 0;
    padding: 0;
    overflow: hidden;
    background: var(--paper);
  }
  .card {
    position: relative;
    width: 1200px;
    height: 741px;
    background: var(--paper);
    font-family: "Arimo", Arial, sans-serif;
    color: var(--ink);
    overflow: hidden;
  }
  .brand {
    position: absolute;
    left: 171px;
    top: 279px;
    width: 316px;
    height: 173px;
    display: flex;
    flex-direction: column;
    align-items: center;
    justify-content: center;
    gap: 10px;
  }
  .brand-dot {
    width: 16px;
    height: 16px;
    border-radius: 50%;
    background: var(--spearmint);
  }
  .brand-name {
    margin: 0;
    font-size: 40px;
    font-weight: 700;
    line-height: 1.05;
    text-align: center;
    color: var(--ink);
  }
  .divider-vertical {
    position: absolute;
    left: 564px;
    top: 242px;
    height: 250px;
    border-left: 2px dotted var(--spearmint);
  }
  .divider-horizontal {
    position: absolute;
    left: 566px;
    top: 334px;
    width: 472px;
    border-top: 2px dotted var(--spearmint);
  }
  .person {
    position: absolute;
    left: 593px;
    top: 258px;
    margin: 0;
    font-size: 45px;
    line-height: 1;
    letter-spacing: -0.5px;
  }
  .person-first { font-weight: 700; color: var(--ink); }
  .person-last { font-weight: 400; color: var(--spearmint); }
  .contact {
    position: absolute;
    left: 593px;
    top: 362px;
    margin: 0;
    padding: 0;
    list-style: none;
    font-size: 28px;
    line-height: 43px;
    color: var(--ink);
  }
  .contact-email-user {
    font-weight: 700;
    color: var(--spearmint);
  }
</style>
</head>
<body>
  <div class="card">
    <div class="brand">
      <span class="brand-dot"></span>
      <p class="brand-name">Velvet Bloom<br>Beauty</p>
    </div>

    <div class="divider-vertical"></div>
    <div class="divider-horizontal"></div>

    <h1 class="person"><span class="person-first">jess</span><span class="person-last">moreton</span></h1>

    <ul class="contact">
      <li class="contact-address">18 Windarra Court Parkhurst</li>
      <li class="contact-phone">0482615097</li>
      <li class="contact-email"><span class="contact-email-user">velvetbloombeauty</span>@mailbox.com</li>
    </ul>
  </div>
</body>
</html>
```